Handyman home maintenance postcard

We would like the postcard to state what we do : Painting, plumbing, electrical, flooring, carpentry, drywall, fencing, windows and more. We would also like our promotion to state : First four hours of work is only $299. Additional hours are 25% off our regular rate of $110 an hour. Rate includes two expert handymen working to complete your job.

Target Market(s)

30-75

Industry/Entity Type

Home maintenance

```html
<!DOCTYPE html>
<html lang="en">
<head>
<meta charset="utf-8">
<title>Steadfast Handyman Services – Postcard</title>
<link rel="stylesheet" href="https://fonts.googleapis.com/css2?family=Oswald:wght@500&family=Roboto+Condensed:wght@700;800&family=Roboto:wght@400;700&display=swap">
<style>
  :root {
    --stage: #2b2b2b;
    --white: #ffffff;
    --ink: #111111;
    --orange: #f7941d;
    --orange-light: #fbab2c;
    --orange-deep: #f07f0c;
    --photo-light: #f4f4f4;
    --photo-mid: #d9d9d9;
  }
  * { box-sizing: border-box; margin: 0; padding: 0; }
  html, body {
    width: 1200px; height: 1177px; overflow: hidden;
    background: var(--stage);
  }
  .postcard {
    position: absolute; left: 152px; top: 294px;
    width: 879px; height: 586px;
    background: var(--white);
    overflow: hidden;
  }
  .crew-photo {
    position: absolute; left: 0; top: 0; width: 502px; height: 302px;
    background: radial-gradient(ellipse at 50% 60%, var(--photo-mid) 0%, var(--photo-light) 55%, var(--white) 100%);
  }
  .brand {
    position: absolute; left: 490px; top: 46px;
    display: flex; align-items: center; gap: 10px;
    white-space: nowrap;
  }
  .brand-dot {
    width: 30px; height: 30px; border-radius: 50%;
    background: var(--orange); flex: none;
  }
  .brand-name {
    font-family: "Roboto Condensed", sans-serif; font-weight: 800;
    font-size: 27px; line-height: 36px; color: var(--ink); letter-spacing: -0.3px;
  }
  .service-list {
    position: absolute; top: 130px; list-style: none;
    font-family: "Roboto Condensed", sans-serif; font-weight: 800;
    font-size: 23px; color: var(--ink); line-height: 29px;
    white-space: nowrap;
  }
  .service-list.col-a { left: 562px; }
  .service-list.col-b { left: 727px; }
  .service-list li { position: relative; padding-left: 16px; }
  .service-list li::before {
    content: ""; position: absolute; left: 0; top: 8px;
    border-left: 9px solid var(--orange);
    border-top: 7px solid transparent; border-bottom: 7px solid transparent;
  }
  .headline-band {
    position: absolute; left: 0; top: 302px; width: 879px; height: 72px;
    background: var(--ink);
    display: flex; align-items: center; justify-content: center;
    font-family: "Oswald", sans-serif; font-weight: 500;
    font-size: 48px; color: var(--white); letter-spacing: 0.5px;
    white-space: nowrap;
  }
  .headline-band .accent { color: var(--orange); }
  .offer-panel {
    position: absolute; left: 0; top: 374px; width: 879px; height: 212px;
    background: linear-gradient(180deg, var(--orange-light) 0%, var(--orange) 55%, var(--orange-deep) 100%);
  }
  .rate-box {
    position: absolute; top: 16px; width: 95px; height: 132px;
    border: 3px solid var(--white); border-radius: 10px; overflow: hidden;
    font-family: "Roboto Condensed", sans-serif; font-weight: 800;
    text-align: center; background: var(--white);
  }
  .rate-box .rate-label {
    height: 86px; background: var(--ink); color: var(--white);
    display: flex; flex-direction: column; justify-content: center;
    font-size: 15px; line-height: 17px; border-radius: 7px 7px 0 0;
  }
  .rate-box .rate-label em { font-style: normal; color: var(--orange); }
  .rate-box .rate-value {
    height: 40px; display: flex; align-items: center; justify-content: center;
    font-size: 28px; color: var(--orange-deep);
  }
  .rate-box.first { left: 43px; }
  .rate-box.additional { left: 151px; }
  .rate-box.regular { left: 257px; }
  .rate-box.additional .rate-label { background: var(--white); color: var(--orange); }
  .rate-box.additional .rate-value {
    background: var(--ink); color: var(--white); font-size: 18px; border-radius: 0 0 7px 7px;
  }
  .crew-note {
    position: absolute; left: 43px; top: 158px; width: 307px; height: 46px;
    border: 2px dashed var(--white); border-radius: 4px;
    display: flex; align-items: center; justify-content: center; text-align: center;
    font-family: "Roboto", sans-serif; font-size: 13px; line-height: 16px; color: var(--ink);
  }
  .quote-call {
    position: absolute; left: 452px; top: 26px; width: 390px;
    font-family: "Roboto", sans-serif; font-size: 31px; line-height: 40px; color: var(--ink);
    white-space: nowrap;
  }
  .quote-call strong { font-weight: 700; }
  .phone-strip {
    position: absolute; left: 442px; top: 77px; width: 406px; height: 66px;
  }
  .phone-strip .strip-shape { position: absolute; left: 0; top: 0; }
  .phone-strip .phone-icon { position: absolute; left: -32px; top: 10px; }
  .phone-number {
    position: absolute; left: 22px; top: 0; height: 66px;
    display: flex; align-items: center;
    font-family: "Roboto Condensed", sans-serif; font-weight: 800;
    font-size: 56px; line-height: 1; color: var(--orange-deep); letter-spacing: 1px;
    white-space: nowrap;
  }
  .web-line {
    position: absolute; left: 401px; top: 162px;
    display: flex; align-items: center; gap: 8px;
    font-family: "Roboto Condensed", sans-serif; font-weight: 800;
    font-size: 27px; line-height: 30px; color: var(--ink);
    white-space: nowrap;
  }
</style>
</head>
<body>
  <main class="postcard">
    <div class="crew-photo" role="img" aria-label="Photo of three handymen in grey overalls and tool belts: one on a ladder, one smiling with a clipboard, one using a drill"></div>

    <div class="brand">
      <span class="brand-dot"></span>
      <span class="brand-name">Steadfast Handyman Services</span>
    </div>

    <ul class="service-list col-a">
      <li>PAINTING</li>
      <li>PLUMBING</li>
      <li>ELECTRICAL</li>
      <li>FLOORING</li>
      <li>CARPENTRY</li>
    </ul>
    <ul class="service-list col-b">
      <li>DRYWALL</li>
      <li>FENCING</li>
      <li>WINDOWS</li>
      <li>AND MORE</li>
    </ul>

    <div class="headline-band">TRUSTED HANDYMAN&nbsp;<span class="accent">&amp; REPAIR SERVICES</span></div>

    <section class="offer-panel">
      <div class="rate-box first">
        <div class="rate-label">FIRST<em>4 HOURS</em>OF WORK<br>IS ONLY</div>
        <div class="rate-value">$299</div>
      </div>
      <div class="rate-box additional">
        <div class="rate-label">ADDITIONAL<br>HOURS<br>ARE</div>
        <div class="rate-value">25% OFF</div>
      </div>
      <div class="rate-box regular">
        <div class="rate-label">OUR<br>REGULAR<br>RATE<br>PER HOUR</div>
        <div class="rate-value">$110</div>
      </div>
      <div class="crew-note">Rate includes two expert handymen<br>working to complete your job.</div>

      <div class="quote-call">Call Us for <strong>FREE</strong> Quotation</div>

      <div class="phone-strip">
        <svg class="strip-shape" width="406" height="66" viewBox="0 0 406 66">
          <polygon points="6,4 406,0 392,66 0,62" fill="#ffffff"/>
        </svg>
        <svg class="phone-icon" width="46" height="46" viewBox="0 0 46 46">
          <circle cx="23" cy="23" r="20" fill="#fbab2c" stroke="#ffffff" stroke-width="3"/>
          <path d="M15 14c0-2 2-3 3-3l3 5-2 2c1 3 4 6 7 7l2-2 5 3c0 1-1 3-3 3-8 0-15-7-15-15z" fill="#111111"/>
        </svg>
        <div class="phone-number">555 014 2287</div>
      </div>

      <div class="web-line">
        <svg width="24" height="24" viewBox="0 0 24 24" fill="none" stroke="#ffffff" stroke-width="2">
          <circle cx="12" cy="12" r="10"/>
          <ellipse cx="12" cy="12" rx="4.5" ry="10"/>
          <line x1="2" y1="12" x2="22" y2="12"/>
        </svg>
        <span>STEADFASTHANDYMANPRO.COM</span>
      </div>
    </section>
  </main>
</body>
</html>
```